GLP letterhead

We need a letterhead design for our new company based in Los Angeles called "Gold Lantern Pictures". We develop film and television projects. We work with investors, financiers, film production companies, film distribution and sales companies as well as studios. We would like to incorporate our logo (see attached) but make the letterhead simple and elegant. We need to include: logo, company address, phone number and company website.
Updates

Hello designers, Thanks for your submissions. For our letterhead, we are looking for something more simple and elegant. No heavy bars or lines. Make it feel light and clean. Not a lot of ink on the page. Use the logo and contact info but think "clean", "streamlined" and mostly white paper. Looking forward to seeing more... thanks! Gold Lantern Pictures team

Target Market(s)

Studio executives, talent agents and agencies, financiers, investors.

Industry/Entity Type

It Company

Requirements
Must have
• Gold Lantern Pictures logo (see attached). Logo may be cropped and altered appropriately for elegant letterhead design.
• Please include:
• COMPANY ADDRESS:
• Ridgeway Studio Park
• 2850 Halverson Street
• Tower Annex, 4th Floor
• Manhattan Beach, CA 90412
• COMPANY WEBSITE:
• www.goldlanternpicturesco.example
• COMPANY PHONE NUMBER:
• 310-555-0148

```html
<!DOCTYPE html>
<html lang="en">
<head>
<meta charset="utf-8">
<title>Gold Lantern Pictures — Letterhead</title>
<link rel="stylesheet" href="https://fonts.googleapis.com/css2?family=Crimson+Pro:wght@400;700&family=Montserrat:wght@600&display=swap">
<style>
  :root {
    --backdrop: #e6e4e1;
    --paper: #ffffff;
    --ink: #2a2a2a;
    --ink-soft: #6b6b6b;
    --brand-cyan: #3a9fc6;
    --brand-deep: #1a4f72;
    --hairline: #c9d6de;
    --divider: #b5b5b5;
  }
  * { box-sizing: border-box; margin: 0; padding: 0; }
  html, body { width: 955px; height: 1200px; overflow: hidden; }
  body { background: var(--backdrop); position: relative; font-family: "Crimson Pro", Georgia, serif; }

  .sheet {
    position: absolute; left: 54px; top: 47px; width: 862px; height: 1115px;
    background: var(--paper);
  }
  .masthead {
    position: absolute; left: 0; top: 0; width: 862px; height: 147px;
    border-bottom: 1px solid var(--hairline);
  }
  .brand {
    position: absolute; left: 20px; top: 24px; width: 200px; text-align: center;
  }
  .brand-mark {
    display: block; width: 46px; height: 46px; margin: 0 auto 8px;
    border-radius: 50%; background: var(--brand-cyan);
  }
  .brand-name {
    font-family: "Montserrat", Arial, sans-serif; font-weight: 600;
    font-size: 15px; letter-spacing: 1px; color: var(--brand-cyan); line-height: 1.15;
  }
  .brand-tagline {
    margin-top: 7px; font-family: "Montserrat", Arial, sans-serif; font-weight: 600;
    font-size: 6.5px; letter-spacing: 1.6px; color: var(--ink-soft);
  }
  .contact-divider {
    position: absolute; left: 559px; top: 53px; width: 1px; height: 75px; background: var(--divider);
  }
  .contact-row { position: absolute; left: 576px; display: flex; gap: 10px; color: var(--ink); }
  .contact-row svg { flex: none; margin-top: 2px; }
  .contact-address { top: 53px; font-size: 15.5px; line-height: 16px; }
  .contact-address address { font-style: normal; }
  .contact-phone { top: 111px; font-size: 15.5px; font-weight: 700; }

  .footer-rule { position: absolute; left: 0; width: 862px; height: 1px; background: var(--hairline); }
  .footer-rule.upper { top: 1054px; }
  .footer-rule.lower { top: 1086px; }
  .footer-line {
    position: absolute; left: 0; top: 1057px; width: 862px; height: 27px;
    display: flex; align-items: center; justify-content: center;
  }
  .website {
    color: var(--brand-deep); font-weight: 700; font-size: 14px; letter-spacing: 1.3px; margin-left: -10px;
  }
</style>
</head>
<body>
  <main class="sheet">
    <header class="masthead">
      <div class="brand">
        <span class="brand-mark"></span>
        <div class="brand-name">GOLD LANTERN<br>PICTURES</div>
        <div class="brand-tagline">A MEDIA ENTERTAINMENT COMPANY</div>
      </div>
      <div class="contact-divider"></div>
      <div class="contact-row contact-address">
        <svg width="14" height="14" viewBox="0 0 14 14" aria-hidden="true">
          <circle cx="7" cy="7" r="7" fill="#3a9fc6"/>
          <path d="M3 7.2 L7 3.6 L11 7.2 M4.5 6.3 V10.5 H9.5 V6.3" fill="none" stroke="#ffffff" stroke-width="1.4"/>
        </svg>
        <address>
          Ridgeway Studio Park<br>
          2850 Halverson Street Tower Annex<br>
          4th Floor Manhattan Beach, CA 90412
        </address>
      </div>
      <div class="contact-row contact-phone">
        <svg width="14" height="14" viewBox="0 0 14 14" aria-hidden="true">
          <circle cx="7" cy="7" r="7" fill="#3a9fc6"/>
          <path d="M5 3.5 C3.6 5.5 4.6 9 8.6 10.6 L9.6 9.2 L8.3 8.2 L7.6 8.9 C6.4 8.2 5.8 7.2 5.7 6.2 L6.5 5.8 L6 3.8 Z" fill="#ffffff"/>
        </svg>
        <span>310-555-0148</span>
      </div>
    </header>

    <div class="footer-rule upper"></div>
    <footer class="footer-line">
      <span class="website">www.goldlanternpicturesco.example</span>
    </footer>
    <div class="footer-rule lower"></div>
  </main>
</body>
</html>
```